Website for business consultancy - bright and happy feel needed

I need a website with 3/4 pages. I want the first page designed first and the rest will be easy. I need some pictures but none with corporate looking people. I need links to quillpost and deskroster. I need a contact form. I have samples of websites i like, fonts i like and I need a small logo also. I like simple, clean lines and I want a bright, happy and feminine feel. My audience are small businesses so I don't want them intimidated by new much of a corporate feel.
Updates

Target Market(s)

Small medium size businesses who want to grow and need that help but they cannot afford a full time financial director.

Industry/Entity Type

Business Consultant

Number of Pages Required

4 page

Other font styles liked:
• i can attach images

Colors
fcf0f6
e667a6
85cae6
ffffff
fbee3e

Requirements
Must have
• Link to quillpost and desk roster
• Contact form linked to my email
• Pictures - full width images where required
• Colour
• Mobile ready
• Soft feminine feel to it
• I dont want it to look like a corporate business consultancy - much more marketing or interior deign feel
Nice to have
• I would like the 3 services I have in 3 boxes that you click and takes you to a place with more information on the service.
• pictures thinking outside of the box
• Can be wordpress if need be
Should not have
• pictures with too much of a corporate feel
• No pictures of coporate people at all
• i like the following websites
• www.marbelquint.co.uk and others that are attached in the documents with a feminine feel to them

```html
<!DOCTYPE html>
<html lang="en">
<head>
<meta charset="utf-8">
<title>Maren Tallis | Consulting</title>
<link href="https://fonts.googleapis.com/css2?family=Saira+Semi+Condensed:wght@300;400&family=Open+Sans:wght@400;600&display=swap" rel="stylesheet">
<style>
:root{
  --rose:#e667a6;
  --rose-deep:#d4528f;
  --rose-soft:#f08cbd;
  --blush:#fcf0f6;
  --sky:#85cae6;
  --sky-deep:#5fb4d8;
  --sun:#fbee3e;
  --ink:#2a2228;
  --text:#4f4a4d;
  --muted:#6e676b;
  --white:#ffffff;
}
*{margin:0;padding:0;box-sizing:border-box}
html,body{width:850px;height:1200px;overflow:hidden;background:var(--white)}
body{position:relative;font-family:"Open Sans",sans-serif;color:var(--text)}
.display{font-family:"Saira Semi Condensed",sans-serif;font-weight:300}
.abs{position:absolute}

/* header */
.site-header{left:0;top:0;width:850px;height:52px;background:var(--white)}
.brand{left:52px;top:12px;font-size:19px;color:var(--rose);white-space:nowrap}
.main-nav{left:435px;top:20px;display:flex;gap:24px;font-size:9px;color:#333;letter-spacing:.2px}
.main-nav .active{color:var(--rose)}
.social{left:756px;top:19px;display:flex;gap:8px;font-size:9px;color:#a0959b}

/* hero */
.hero{left:0;top:52px;width:850px;height:397px;
  background:linear-gradient(100deg,#3a3530 0%,#6b5a48 30%,#b39c8c 55%,#7d7a86 78%,#3c3a48 100%)}
.hero-title{left:52px;top:218px;width:360px;font-size:21px;line-height:23px;color:var(--white)}
.touch-tab{left:816px;top:187px;width:34px;height:128px;background:var(--rose);border-radius:3px 0 0 3px}
.touch-tab span{position:absolute;left:10px;top:88px;transform:rotate(-90deg);transform-origin:0 0;
  font-size:10px;font-weight:600;color:var(--white);white-space:nowrap;letter-spacing:.3px}
.touch-tab svg{position:absolute;left:9px;top:97px}

/* welcome */
.welcome{left:0;top:476px;width:850px;text-align:center}
.welcome h1{font-size:18px;color:var(--ink);font-weight:300}
.welcome h1 em{font-style:normal;color:var(--rose)}
.welcome .lead{margin-top:3px;font-size:11.5px;color:var(--muted)}
.welcome .body{margin:16px auto 0;width:650px;font-size:9.5px;line-height:17px;color:var(--text)}

/* service cards */
.card{top:594px;width:236px;height:157px;color:var(--white);text-align:center}
.card::before{content:"";position:absolute;left:0;top:0;border-style:solid;border-width:16px 16px 0 0;border-color:var(--sun) transparent transparent transparent}
.card-1{left:52px;background:var(--rose)}
.card-2{left:307px;background:var(--sky-deep)}
.card-3{left:562px;background:var(--rose-soft)}
.card h2{margin:22px auto 0;width:200px;font-size:16px;line-height:20px;font-weight:300}
.card p{margin-top:31px;font-size:13px;font-family:"Saira Semi Condensed",sans-serif;font-weight:300}

/* contact band */
.cta{left:0;top:784px;width:850px;height:170px;
  background:linear-gradient(90deg,#d7e9f2,#f3dbe7 45%,#f8e4ee 52%,#f3dbe7 60%,#d7e9f2)}
.cta-content{left:0;top:822px;width:850px;text-align:center}
.cta-content h2{font-size:18.5px;color:var(--ink);font-weight:300}
.cta-content p{margin-top:5px;font-size:11.5px;color:#5a5358}
.cta-button{left:354px;top:876px;width:141px;height:38px;border-radius:19px;background:var(--rose);
  color:var(--white);font-size:13px;line-height:38px;text-align:center}

/* footer */
.footer{left:0;top:954px;width:850px;height:209px;background:var(--blush)}
.col-title{font-size:13px;color:var(--ink)}
.field{background:var(--white);font-size:9.5px;color:#a0979c;padding:6px 8px}
.submit{left:52px;top:1110px;width:75px;height:26px;background:var(--rose);color:var(--white);
  font-size:9.5px;font-weight:600;text-align:center;line-height:26px}
.contact-info{left:370px;top:1010px;font-size:10px;line-height:14.5px;color:#4a4347;font-style:normal}
.contact-info strong{font-weight:600}
.map{left:562px;top:1009px;width:236px;height:108px;
  background:linear-gradient(135deg,#efe6cc,#e4dccb 40%,#f2e27a 60%,#e6dcc6)}
.copyright{left:0;top:1174px;width:850px;text-align:center;font-size:10px;color:#5a5358}
</style>
</head>
<body>

<header class="abs site-header">
  <div class="abs brand display">Maren Tallis | Consulting</div>
  <nav class="abs main-nav">
    <span class="active">HOME</span><span>ABOUT</span><span>SERVICES</span><span>BLOG</span><span>CONTACT US</span>
  </nav>
  <div class="abs social"><span>quillpost</span><span>deskroster</span></div>
</header>

<section class="abs hero" role="img" aria-label="Photo of three colleagues smiling while looking at a tablet in a café"></section>
<p class="abs hero-title display">Lorem Ipsum is simply dummy text of the printing and typesetting industry.</p>
<a class="abs touch-tab">
  <span>GET IN TOUCH</span>
  <svg width="16" height="16" viewBox="0 0 16 16"><path d="M8 1a7 7 0 1 0 0 14h7V8A7 7 0 0 0 8 1z" fill="#fff"/></svg>
</a>

<section class="abs welcome">
  <h1 class="display">Welcome to <em>Maren Tallis | Consulting</em></h1>
  <p class="lead">Not all businesses can afford to hire an accountant full time.</p>
  <p class="body">Lorem Ipsum is simply dummy text of the printing and typesetting industry. Lorem Ipsum has been the industry's standard dummy text ever since the 1500s, when an unknown printer took a galley of type and scrambled it to make a type specimen book.</p>
</section>

<article class="abs card card-1"><h2 class="display">Lorem Ipsum is simply dummy text of the printing and typesetting industry.</h2><p>Maren Tallis I Consulting</p></article>
<article class="abs card card-2"><h2 class="display">Lorem Ipsum is simply dummy text of the printing and typesetting industry.</h2><p>Maren Tallis I Consulting</p></article>
<article class="abs card card-3"><h2 class="display">Lorem Ipsum is simply dummy text of the printing and typesetting industry.</h2><p>Maren Tallis I Consulting</p></article>

<section class="abs cta" role="img" aria-label="Faded photo of people in silhouette at a meeting table against city windows"></section>
<div class="abs cta-content">
  <h2 class="display">Need More details? Contact Us Today!</h2>
  <p>We are here to assist. Contact us by email or via our social media.</p>
</div>
<a class="abs cta-button display">Contact Us Today</a>

<footer class="abs footer"></footer>
<h3 class="abs col-title display" style="left:52px;top:982px">Leave A Message</h3>
<div class="abs field" style="left:52px;top:1012px;width:141px;height:27px">Name</div>
<div class="abs field" style="left:199px;top:1012px;width:141px;height:27px">Email</div>
<div class="abs field" style="left:52px;top:1046px;width:288px;height:58px">Message</div>
<div class="abs submit">SUBMIT</div>

<h3 class="abs col-title display" style="left:370px;top:982px">Contact Information</h3>
<address class="abs contact-info">
  <strong>Maren Tallis | Consulting</strong><br>
  228, Company name, Street name,<br>
  City name - 218548<br><br>
  T: 1800 555 0142<br>
  F: 1800 555 0143<br>
  E: info@marentallisconsulting.com
</address>

<h3 class="abs col-title display" style="left:562px;top:982px">Location Map</h3>
<div class="abs map" role="img" aria-label="Street map showing the office location"></div>

<p class="abs copyright">Copyright ©2016 Maren Tallis | Consulting. Terms of Use | Privacy Policy</p>

</body>
</html>
```